Wine Company Flyer Design

Hello,

I need a flyer design that will fit an 11 inch width by 17 inch height. Design has to be submitted in PDF X-1a format.

We want our logo on the flyer with the slogan underneath it saying "Better Wines Lower Prices"

We want a nice design and then we will get to some of the text that will be on the flyer.

Please make the flyer in two colors ONLY. Use the colors of our logo for the rest of the design.

Requirements
Must have
• PDF x-1a format
• Logo on flyer with slogan "Better Wines Lower Prices" underneath
• Two colors - Orange, Red (Same as logo colors)
• Fits in an 11"x17" format for printing
• This will be for the wine industry so include elements of wine in the flyer and make it look nice. Leave some space in the middle of the design for text to be put in.

```html
<!DOCTYPE html>
<html lang="en">
<head>
<meta charset="utf-8">
<title>VinoValue Flyer</title>
<link href="https://fonts.googleapis.com/css2?family=Oswald:wght@600;700&family=Varela+Round&family=Nunito:wght@400;800&display=swap" rel="stylesheet">
<style>
  :root {
    --backdrop: #5a5a5c;
    --paper: #ffffff;
    --wine-red: #e3151d;
    --wine-orange: #f29400;
  }
  html, body {
    margin: 0;
    padding: 0;
    width: 1200px;
    height: 1200px;
    overflow: hidden;
    background: var(--backdrop);
  }
  .flyer {
    position: absolute;
    left: 274px;
    top: 93px;
    width: 651px;
    height: 1013px;
    background: var(--paper);
    overflow: hidden;
    box-shadow: 6px 6px 8px rgba(0,0,0,0.45);
  }
  .brand-circle {
    position: absolute;
    top: 30px;
    left: 275px;
  }
  .brand-name {
    position: absolute;
    top: 128px;
    left: 0;
    width: 100%;
    margin: 0;
    text-align: center;
    font-family: "Oswald", sans-serif;
    font-weight: 700;
    font-size: 46px;
    line-height: 52px;
    color: var(--wine-red);
  }
  .slogan {
    position: absolute;
    top: 204px;
    left: 0;
    width: 100%;
    height: 40px;
    margin: 0;
    display: flex;
    justify-content: center;
    align-items: flex-end;
    gap: 12px;
    font-family: "Varela Round", sans-serif;
    font-size: 27px;
    line-height: 34px;
    letter-spacing: 1px;
    color: var(--wine-orange);
  }
  .slogan .glass-icon { margin-bottom: 4px; }
  .thanks {
    position: absolute;
    top: 253px;
    left: 0;
    width: 100%;
    margin: 0;
    text-align: center;
    font-family: "Oswald", sans-serif;
    font-weight: 600;
    font-size: 20px;
    line-height: 28px;
    letter-spacing: 1.5px;
    color: var(--wine-red);
  }
  .perks {
    margin: 0;
    padding: 0;
    list-style: none;
    font-family: "Nunito", sans-serif;
    font-size: 21px;
    line-height: 26px;
    color: var(--wine-red);
  }
  .perk {
    position: absolute;
    left: 106px;
    display: flex;
    align-items: center;
    gap: 18px;
  }
  .perk-stock { top: 323px; }
  .perk-shipping { top: 380px; }
  .perk-mix { top: 451px; }
  .perk-gift { top: 530px; }
  .perk-icon { flex: none; }
  .promo-code { color: var(--wine-orange); }
  .website {
    position: absolute;
    top: 642px;
    left: 0;
    width: 100%;
    margin: 0;
    text-align: center;
    font-family: "Nunito", sans-serif;
    font-weight: 800;
    font-size: 26px;
    line-height: 32px;
    color: var(--wine-red);
  }
  .bottle-row {
    position: absolute;
    left: 0;
    bottom: 0;
    width: 100%;
    height: 300px;
    background:
      linear-gradient(180deg, rgba(255,255,255,1) 0%, rgba(255,255,255,0) 28%),
      linear-gradient(90deg, var(--wine-red) 0%, var(--wine-orange) 15%, var(--wine-red) 28%, var(--wine-orange) 40%, var(--wine-red) 50%, var(--wine-orange) 62%, var(--wine-red) 75%, var(--wine-orange) 88%, var(--wine-red) 100%);
  }
</style>
</head>
<body>
  <main class="flyer">
    <svg class="brand-circle" width="101" height="101" viewBox="0 0 101 101" aria-hidden="true">
      <circle cx="50.5" cy="50.5" r="46" fill="none" stroke="var(--wine-orange)" stroke-width="8"/>
    </svg>
    <h1 class="brand-name">VINOVALUE</h1>

    <p class="slogan">
      <span>Better Wines</span>
      <svg class="glass-icon" width="20" height="37" viewBox="0 0 22 42" aria-hidden="true">
        <path d="M2 2 H20 V12 A9 10 0 0 1 2 12 Z" fill="none" stroke="var(--wine-red)" stroke-width="2"/>
        <path d="M2.5 9 H19.5 V12 A8.5 9.5 0 0 1 2.5 12 Z" fill="var(--wine-red)"/>
        <path d="M11 22 V38 M4 39 H18" stroke="var(--wine-red)" stroke-width="2.5"/>
      </svg>
      <span>Lower Prices</span>
    </p>

    <h2 class="thanks">THANK YOU FOR YOUR ORDER!</h2>

    <ul class="perks">
      <li class="perk perk-stock">
        <svg class="perk-icon" width="18" height="34" viewBox="0 0 22 42" aria-hidden="true"><path d="M2 2 H20 V12 A9 10 0 0 1 2 12 Z" fill="none" stroke="var(--wine-red)" stroke-width="2"/><path d="M2.5 9 H19.5 V12 A8.5 9.5 0 0 1 2.5 12 Z" fill="var(--wine-red)"/><path d="M11 22 V38 M4 39 H18" stroke="var(--wine-red)" stroke-width="2.5"/></svg>
        <span>100's of Popular and Collector Wines in Stock.</span>
      </li>
      <li class="perk perk-shipping">
        <svg class="perk-icon" width="18" height="34" viewBox="0 0 22 42" aria-hidden="true"><path d="M2 2 H20 V12 A9 10 0 0 1 2 12 Z" fill="none" stroke="var(--wine-red)" stroke-width="2"/><path d="M2.5 9 H19.5 V12 A8.5 9.5 0 0 1 2.5 12 Z" fill="var(--wine-red)"/><path d="M11 22 V38 M4 39 H18" stroke="var(--wine-red)" stroke-width="2.5"/></svg>
        <span>Free Shipping on 6 Packs or More.<br>Use Code <span class="promo-code">"Shipfree1"</span> at Checkout.</span>
      </li>
      <li class="perk perk-mix">
        <svg class="perk-icon" width="18" height="34" viewBox="0 0 22 42" aria-hidden="true"><path d="M2 2 H20 V12 A9 10 0 0 1 2 12 Z" fill="none" stroke="var(--wine-red)" stroke-width="2"/><path d="M2.5 9 H19.5 V12 A8.5 9.5 0 0 1 2.5 12 Z" fill="var(--wine-red)"/><path d="M11 22 V38 M4 39 H18" stroke="var(--wine-red)" stroke-width="2.5"/></svg>
        <span>Mix and Match 1 to 18 Bottles<br>For Yourself or as a Gift.</span>
      </li>
      <li class="perk perk-gift">
        <svg class="perk-icon" width="18" height="34" viewBox="0 0 22 42" aria-hidden="true"><path d="M2 2 H20 V12 A9 10 0 0 1 2 12 Z" fill="none" stroke="var(--wine-red)" stroke-width="2"/><path d="M2.5 9 H19.5 V12 A8.5 9.5 0 0 1 2.5 12 Z" fill="var(--wine-red)"/><path d="M11 22 V38 M4 39 H18" stroke="var(--wine-red)" stroke-width="2.5"/></svg>
        <span>Custom Gift Announcements Available.</span>
      </li>
    </ul>

    <p class="website">www.VinoValue.com</p>

    <div class="bottle-row" role="img" aria-label="Row of overlapping wine bottle silhouettes in alternating orange and red"></div>
  </main>
</body>
</html>
```